Business Card Design Project

Maid Cleaning Services
Tidy Haven Cleaning Services
5550147268
tidyhavencleaning@examplemail.test
facebook - tidy haven

Business

We would really like a card that the shape of a made.
That would be great.
I would love to see how that would look.

```html
<!DOCTYPE html>
<html lang="en">
<head>
<meta charset="utf-8">
<title>Tidy Haven Cleaning Services – Business Card</title>
<link rel="stylesheet" href="https://fonts.googleapis.com/css2?family=Open+Sans:wght@600&family=Gelasio:wght@400&display=swap">
<style>
  :root {
    --backdrop: #e9e9e9;
    --card-white: #f4f4f5;
    --purple: #6f3d9e;
    --purple-light: #8a5cb8;
    --green: #3cb54a;
    --ink-purple: #5b2d8a;
  }
  * { margin: 0; padding: 0; box-sizing: border-box; }
  html, body { width: 1200px; height: 800px; overflow: hidden; }
  body {
    background: var(--backdrop);
    position: relative;
    font-family: "Gelasio", Georgia, serif;
  }
  .card {
    position: absolute;
    width: 500px;
    height: 286px;
    background: var(--card-white);
    box-shadow: 0 10px 24px rgba(0,0,0,0.18);
    overflow: hidden;
  }
  .card--front { left: 70px; top: 257px; }
  .card--back { left: 630px; top: 257px; }
  .card__art { position: absolute; inset: 0; width: 100%; height: 100%; }
  .brand-mark {
    position: absolute;
    display: flex;
    align-items: center;
    gap: 10px;
    font-family: "Open Sans", Arial, sans-serif;
    font-weight: 600;
    color: var(--purple);
    white-space: nowrap;
  }
  .brand-mark__dot {
    border-radius: 50%;
    background: var(--green);
    flex: none;
  }
  .card--front .brand-mark { left: 0; right: 0; top: 82px; justify-content: center; font-size: 40px; }
  .card--front .brand-mark__dot { width: 22px; height: 22px; }
  .card--back .brand-mark { left: 42px; top: 150px; font-size: 22px; gap: 7px; }
  .card--back .brand-mark__dot { width: 13px; height: 13px; }
  .contact {
    position: absolute;
    left: 200px;
    top: 136px;
    color: var(--ink-purple);
  }
  .contact__title {
    font-family: "Open Sans", Arial, sans-serif;
    font-weight: 600;
    font-size: 22px;
    color: var(--green);
    margin-bottom: 8px;
    white-space: nowrap;
    text-shadow: 0 1px 2px rgba(0,0,0,0.15);
  }
  .contact__line {
    display: flex;
    align-items: center;
    gap: 7px;
    font-size: 13px;
    line-height: 21px;
    white-space: nowrap;
  }
  .contact__line--name { padding-left: 19px; }
  .contact__icon { width: 12px; height: 12px; flex: none; fill: var(--ink-purple); }
</style>
</head>
<body>
  <section class="card card--front" aria-label="Card front">
    <svg class="card__art" viewBox="0 0 500 286" preserveAspectRatio="none" aria-hidden="true">
      <defs>
        <linearGradient id="front-purple" x1="0" y1="0" x2="0" y2="1">
          <stop offset="0" stop-color="#7a48a8"/>
          <stop offset="1" stop-color="#6a3a99"/>
        </linearGradient>
      </defs>
      <rect width="500" height="286" fill="url(#front-purple)"/>
      <polygon points="0,0 500,0 500,110 300,256 0,118" fill="#f4f4f5"/>
      <polyline points="14,0 14,122 298,242 486,104 486,0" fill="none" stroke="#6f3d9e" stroke-width="2.5"/>
    </svg>
    <div class="brand-mark"><span class="brand-mark__dot"></span>Tidy Haven</div>
  </section>

  <section class="card card--back" aria-label="Card back">
    <svg class="card__art" viewBox="0 0 500 286" preserveAspectRatio="none" aria-hidden="true">
      <defs>
        <linearGradient id="back-purple" x1="0" y1="0" x2="1" y2="0">
          <stop offset="0" stop-color="#7b4aa8"/>
          <stop offset="1" stop-color="#9464c0"/>
        </linearGradient>
      </defs>
      <rect width="500" height="286" fill="url(#back-purple)"/>
      <polygon points="0,286 0,150 200,28 500,150 500,286" fill="#f4f4f5"/>
      <polyline points="14,286 14,158 202,42 486,158 486,286" fill="none" stroke="#6f3d9e" stroke-width="2.5"/>
    </svg>
    <div class="brand-mark"><span class="brand-mark__dot"></span>Tidy Haven</div>
    <div class="contact">
      <h1 class="contact__title">Home Cleaning Services</h1>
      <p class="contact__line contact__line--name">Tidy Haven Cleaning Services</p>
      <p class="contact__line">
        <svg class="contact__icon" viewBox="0 0 24 24" aria-hidden="true"><path d="M6.6 10.8a15.1 15.1 0 0 0 6.6 6.6l2.2-2.2a1 1 0 0 1 1-.25 11.4 11.4 0 0 0 3.6.57 1 1 0 0 1 1 1V20a1 1 0 0 1-1 1A17 17 0 0 1 3 4a1 1 0 0 1 1-1h3.5a1 1 0 0 1 1 1c0 1.25.2 2.45.57 3.57a1 1 0 0 1-.25 1z"/></svg>
        5550147268
      </p>
      <p class="contact__line">
        <svg class="contact__icon" viewBox="0 0 24 24" aria-hidden="true"><circle cx="12" cy="12" r="11"/><text x="12" y="16.5" text-anchor="middle" font-size="13" font-family="Arial, sans-serif" font-weight="700" fill="#f4f4f5">@</text></svg>
        tidyhavencleaning@examplemail.test
      </p>
    </div>
  </section>
</body>
</html>
```